Brambys Burgers and Tacos needs a new menu board design

We are a fast casual restaurant that sells burgers, tacos, wraps and other items. We have a California feel, sleek and modern, décor has photos of people like Pelliver, Marsk, Dorvale. Song list varies from Copper Wheels, Lantern Moth, Quivers, Halloway Ferrystone etc... Our main goal for this project is to clean up the look of our menu boards...make them easier to read and more reflective of the style of the restaurant. We also want to feature our combos which are our high profit items...think they should take up 30 to 40% of the space.

We have t-shirts that say "Don't Worry Be Hippy", "Hold On Brighter Days", "Make Tacos Not War".

There is potential for other projects such as outdoor menu panels, paper menus, promotional items. I am attaching a layout of the menu panels as they appear now with dimensions. Also photos of the restaurant. We are not planning to use these same panels so please don't design around them...come up with your own ideas on this....there is a slightly curved background. We have a really good sign person that can customize if need be.

We have had this menu for a long time and it needs to be clean and sleek.

Target Market(s)

teenagers to 40+

Industry/Entity Type

Restaurant

Requirements
Must have
• Clean readable headers

```html
<!DOCTYPE html>
<html lang="en">
<head>
<meta charset="utf-8">
<title>Brambys Burgers Menu Board</title>
<link rel="stylesheet" href="https://fonts.googleapis.com/css2?family=Satisfy&family=Passion+One:wght@400&family=Zilla+Slab:wght@300&display=swap">
<style>
  :root {
    --board-dark: #2a2a2b;
    --board-glow: #4b4b4c;
    --frame-grey: #8a8a8a;
    --rule-grey: #8c8c8c;
    --chalk: #f1ede4;
    --chalk-soft: #e2ded6;
    --title-coral: #f0625b;
    --bun: #f6ac3a;
    --patty: #7a3e2a;
    --lettuce: #4dbf7c;
  }
  * { margin: 0; padding: 0; box-sizing: border-box; }
  html, body {
    width: 846px; height: 1200px; overflow: hidden;
    background: var(--board-dark);
  }
  .menu-board {
    position: relative; width: 846px; height: 1200px;
    background: radial-gradient(ellipse 60% 45% at 50% 45%, var(--board-glow) 0%, var(--board-dark) 100%);
    color: var(--chalk);
  }
  .outer-frame {
    position: absolute; left: 26px; top: 26px; width: 794px; height: 1148px;
    border: 4px solid var(--frame-grey); border-radius: 26px;
  }
  .inner-frame {
    position: absolute; left: 47px; top: 71px; width: 753px; height: 1065px;
    border: 2px solid var(--frame-grey);
  }
  .burger-art {
    position: absolute; left: 106px; top: 89px; width: 206px; height: 134px;
  }
  .section-title {
    position: absolute; left: 352px; top: 140px;
    font-family: "Satisfy", cursive; font-size: 82px; line-height: 1;
    color: var(--title-coral);
  }
  .title-rule {
    position: absolute; left: 108px; top: 262px; width: 607px; height: 3px;
    background: var(--rule-grey);
  }
  .menu-item { position: absolute; left: 98px; }
  .item-head {
    display: flex; align-items: baseline; gap: 50px;
  }
  .item-name {
    font-family: "Satisfy", cursive; font-size: 45px; line-height: 1;
    color: var(--chalk);
  }
  .item-price {
    font-family: "Passion One", sans-serif; font-size: 42px; line-height: 1;
    color: var(--chalk); letter-spacing: 0.5px;
  }
  .item-desc {
    margin-top: 8px;
    font-family: "Zilla Slab", serif; font-weight: 300; font-size: 22px; line-height: 30px;
    color: var(--chalk-soft); width: 620px;
  }
  .addon {
    position: absolute; left: 138px; top: 802px;
    display: flex; align-items: baseline; gap: 44px;
  }
  .addon .item-name { font-size: 37px; }
</style>
</head>
<body>
<main class="menu-board">
  <div class="outer-frame"></div>
  <div class="inner-frame"></div>

  <svg class="burger-art" viewBox="0 0 206 134" role="img" aria-label="Burger illustration">
    <rect x="0" y="0" width="206" height="134" rx="40" fill="var(--bun)"/>
  </svg>

  <h1 class="section-title">Burgers</h1>
  <div class="title-rule"></div>

  <section class="menu-item" style="top:300px">
    <div class="item-head"><span class="item-name">Bramby Cheeseburger</span><span class="item-price">5.89 $</span></div>
    <p class="item-desc">Swiss or Cheddar Choice of lettuce, tomato</p>
  </section>

  <section class="menu-item" style="top:427px">
    <div class="item-head"><span class="item-name">Jalapeno Burger</span><span class="item-price">5.89 $</span></div>
    <p class="item-desc">Swiss or Cheddar Choice of lettuce, tomato</p>
  </section>

  <section class="menu-item" style="top:554px">
    <div class="item-head"><span class="item-name">Bacon Cheeseburger</span><span class="item-price">6.99 $</span></div>
    <p class="item-desc">Swiss or Cheddar Choice of lettuce, tomato</p>
  </section>

  <section class="menu-item" style="top:671px">
    <div class="item-head"><span class="item-name">Bleu Cheese Burger</span><span class="item-price">6.49 $</span></div>
    <p class="item-desc">Bramby’s Bleu Cheese blend of crumbles and dressing, lettuce, tomato</p>
  </section>

  <div class="addon">
    <span class="item-name">more better. . . add Bacon</span><span class="item-price">0.99 $</span>
  </div>

  <section class="menu-item" style="top:872px">
    <div class="item-head" style="gap:22px"><span class="item-name">Mushroom Swiss Burger</span><span class="item-price">6.49 $</span></div>
    <p class="item-desc" style="width:460px">Fresh Grilled Mushrooms, covered with Melted Swiss Cheese</p>
  </section>

  <section class="menu-item" style="top:1024px">
    <div class="item-head"><span class="item-name">Bacon Cheeseburger</span><span class="item-price">6.99 $</span></div>
    <p class="item-desc">Swiss or Cheddar Choice of lettuce, tomato</p>
  </section>
</main>
</body>
</html>
```